Business card design needed for Automotive Reconditioning business

I have a logo design i just cant decide on the best color or layout for the business card, I will upload all the files so you can see all colors schemes we are considering. I have other file formats if needed let me know.

Target Market(s)

automotive dealerships

Contact Information for Business Card

HERE are the Descriptions and info needed on the card:
Interior Repair: Leather carpet burns panels dash Deoderize
Dealer products and Vin Verify
( spot for name and cell number) My name is Norman Bexley phone 614 352-4180 Title COO www.QuorvalMotive.com

Font styles to use
Sans Serif
Other font styles liked:
• what ever you think looks best

Requirements
Must have
• Must be able to change the name and phone for employees

```html
<!DOCTYPE html>
<html lang="en">
<head>
<meta charset="utf-8">
<title>Quorval Motive – Business Card</title>
<link rel="stylesheet" href="https://fonts.googleapis.com/css2?family=Raleway:wght@500;600;700;800&display=swap">
<style>
  :root {
    --backdrop: #d8d5d1;
    --card-dark: #434241;
    --card-light: #5d5c5b;
    --lime: #8dc63f;
    --ink-light: #ffffff;
    --ink-muted: #e6e6e6;
    --rule: #c9c9c9;
    --pill-ink: #1f2a12;
  }
  * { box-sizing: border-box; margin: 0; padding: 0; }
  html, body {
    width: 1200px;
    height: 1200px;
    overflow: hidden;
    background: var(--backdrop);
    font-family: "Raleway", sans-serif;
  }
  .canvas {
    position: relative;
    width: 1200px;
    height: 1200px;
  }
  .card {
    position: absolute;
    left: 75px;
    top: 286px;
    width: 1050px;
    height: 627px;
    border-radius: 22px;
    background: radial-gradient(ellipse at 62% 38%, var(--card-light) 0%, var(--card-dark) 70%);
    color: var(--ink-light);
    overflow: hidden;
  }
  .accent-bar {
    position: absolute;
    top: 125px;
    height: 77px;
  }
  .accent-bar--lime { left: 94px; width: 13px; background: var(--lime); }
  .accent-bar--pale { left: 118px; width: 14px; background: var(--ink-muted); }

  .person-name {
    position: absolute;
    left: 164px;
    top: 124px;
    font-size: 35px;
    font-weight: 700;
    line-height: 1;
    letter-spacing: 0.3px;
    text-transform: uppercase;
  }
  .person-title {
    position: absolute;
    left: 174px;
    top: 172px;
    font-size: 28px;
    font-weight: 500;
    line-height: 1;
    color: var(--ink-muted);
  }

  .brand {
    position: absolute;
    right: 81px;
    top: 138px;
    display: flex;
    align-items: center;
    gap: 14px;
  }
  .brand-mark {
    width: 22px;
    height: 22px;
    background: var(--lime);
  }
  .brand-name {
    font-size: 38px;
    font-weight: 800;
    line-height: 1;
    letter-spacing: 1px;
    color: var(--ink-light);
    text-transform: uppercase;
  }

  .divider {
    position: absolute;
    left: 70px;
    width: 910px;
    height: 2px;
    background: var(--rule);
  }
  .divider--upper { top: 264px; }
  .divider--lower { top: 275px; }

  .services {
    position: absolute;
    left: 95px;
    top: 300px;
    width: 520px;
    font-size: 27px;
    font-weight: 500;
    line-height: 38px;
    color: var(--ink-light);
  }
  .services strong { font-weight: 700; }

  .offer-pill {
    position: absolute;
    left: 94px;
    top: 391px;
    width: 476px;
    height: 49px;
    background: var(--lime);
    border-radius: 6px 24px 6px 24px;
    color: var(--pill-ink);
    font-size: 27px;
    font-weight: 700;
    line-height: 49px;
    padding-left: 14px;
  }

  .contact-line {
    position: absolute;
    right: 84px;
    display: flex;
    align-items: center;
    gap: 22px;
    font-size: 28px;
    font-weight: 600;
    line-height: 1;
  }
  .contact-line--phone { top: 459px; right: 81px; }
  .contact-line--web { top: 511px; right: 81px; }
  .contact-line svg { width: 36px; height: 36px; flex: none; }
  .web-domain { color: var(--lime); }
</style>
</head>
<body>
<main class="canvas">
  <section class="card" aria-label="Business card">
    <span class="accent-bar accent-bar--lime"></span>
    <span class="accent-bar accent-bar--pale"></span>
    <h1 class="person-name">Norman Bexley</h1>
    <p class="person-title">COO</p>

    <div class="brand">
      <span class="brand-mark"></span>
      <span class="brand-name">Quorval Motive</span>
    </div>

    <span class="divider divider--upper"></span>
    <span class="divider divider--lower"></span>

    <p class="services"><strong>Interior Repair:</strong> Leather carpet burns panels dash Deoderize</p>
    <p class="offer-pill">Dealer products and Vin Verify</p>

    <p class="contact-line contact-line--phone">
      <span>614 352-4180</span>
      <svg viewBox="0 0 24 24" aria-hidden="true">
        <path fill="#8dc63f" d="M6.6 10.8c1.4 2.8 3.8 5.1 6.6 6.6l2.2-2.2c.3-.3.7-.4 1-.2 1.1.4 2.3.6 3.6.6.6 0 1 .4 1 1V20c0 .6-.4 1-1 1C10.6 21 3 13.4 3 4c0-.6.4-1 1-1h3.5c.6 0 1 .4 1 1 0 1.3.2 2.5.6 3.6.1.3 0 .7-.2 1L6.6 10.8z"/>
      </svg>
    </p>
    <p class="contact-line contact-line--web">
      <span>www.<span class="web-domain">QuorvalMotive</span>.com</span>
      <svg viewBox="0 0 24 24" aria-hidden="true">
        <circle cx="12" cy="12" r="10.5" fill="#8dc63f"/>
        <g fill="none" stroke="#434241" stroke-width="1.4">
          <ellipse cx="12" cy="12" rx="4.5" ry="10.5"/>
          <line x1="1.5" y1="12" x2="22.5" y2="12"/>
          <path d="M3.5 7h17M3.5 17h17"/>
        </g>
      </svg>
    </p>
  </section>
</main>
</body>
</html>
```